Dynamic Templates

Our company hosts web stores for our clients. They can set up as many as they wish on our platform, and select from the stock templates we provide. We are looking to increase the number of available stock templates.

Because our users can dynamically control many of the template elements - specifically colors - they have to be flexible and abide by certain rules. These rules are spelled out in the attached documents.

Here are links to two of our most used templates:
http://fernridge.vexalcart.example/
http://stampled.vexalcart.example/

Templates need to have a landing page (what you see when first clicking one of the above links). There also needs to be a category page (what you see when clicking any category) and a product detail page (what you see when you arrive at an individual product, where there are various cart options like Buy Now or Request Info).

```html
<!DOCTYPE html>
<html lang="en">
<head>
<meta charset="utf-8">
<title>Promotional Products Store</title>
<link href="https://fonts.googleapis.com/css2?family=Didact+Gothic&display=swap" rel="stylesheet">
<style>
:root{
  --sky-light:#c4ecfc;
  --sky-mid:#9fd3ea;
  --sky-dark:#2f4f60;
  --bar-grey:#d2d2d2;
  --content-top:#c9c9c9;
  --content-bottom:#a6a6a6;
  --ink:#111;
  --logo-ink:#2b2b2b;
  --tagline-ink:#8a8a8a;
  --link-navy:#0a0a5a;
  --link-blue:#1a1aff;
  --rule:#333;
  --white:#fff;
}
*{margin:0;padding:0;box-sizing:border-box}
html,body{width:1200px;height:960px;overflow:hidden}
body{font-family:"Didact Gothic",sans-serif;color:var(--ink);position:relative;background:var(--white)}

.site-header{position:absolute;left:0;top:0;width:1200px;height:106px;
  background:linear-gradient(to bottom,var(--sky-mid) 0%,var(--sky-light) 45%,var(--sky-light) 70%,var(--sky-mid) 88%,var(--sky-dark) 100%)}
.brand-name{position:absolute;left:130px;top:2px;font-size:52px;line-height:62px;color:var(--logo-ink);letter-spacing:.2px;text-shadow:2px 2px 2px rgba(0,0,0,.25)}
.brand-tagline{position:absolute;left:130px;top:55px;font-size:25px;line-height:30px;color:var(--tagline-ink);letter-spacing:.3px;text-shadow:1px 1px 1px rgba(0,0,0,.25)}

.contact-bar{position:absolute;left:0;top:106px;width:1200px;height:54px;background:var(--bar-grey);border-bottom:2px solid var(--rule)}
.contact-line{position:absolute;right:137px;top:8px;font-size:13px;line-height:17px}
.contact-line .user{font-weight:bold}
.contact-line .phone{font-style:italic}
.contact-line a{color:var(--link-blue);text-decoration:none}

.showcase{position:absolute;left:0;top:162px;width:1200px;height:264px;
  background:linear-gradient(to bottom,#e8e8e8 0%,var(--white) 8%,var(--white) 88%,#dcdcdc 100%);border-bottom:2px solid var(--rule)}
.product-photo{position:absolute;border-radius:4px}
.photo-mousepad{left:133px;top:48px;width:198px;height:176px;background:linear-gradient(to bottom,#b3242c,#8e1a20)}
.photo-cooler{left:372px;top:42px;width:198px;height:184px;background:linear-gradient(to bottom,#6a6a6a,#2a2a2a 60%,#bdbdbd)}
.photo-umbrella{left:648px;top:66px;width:200px;height:134px;background:linear-gradient(to bottom,#3a6fc0,#8fb0dc)}
.photo-candy{left:885px;top:20px;width:164px;height:228px;background:linear-gradient(to bottom,#e9e4d8,#e4a85a 45%,#d86a4a)}

.welcome{position:absolute;left:0;top:428px;width:1200px;height:320px;
  background:linear-gradient(to bottom,var(--content-top),var(--content-bottom));border-bottom:2px solid var(--rule)}
.welcome-inner{position:absolute;left:129px;top:6px;width:948px}
.welcome h1,.welcome h2{font-weight:normal;font-size:24px;line-height:30px;letter-spacing:.3px;text-shadow:1px 1px 1px rgba(255,255,255,.6)}
.welcome p{font-size:15px;line-height:17px;letter-spacing:.25px;text-shadow:1px 1px 0 rgba(255,255,255,.4)}
.welcome .intro{margin-top:10px}
.welcome .pitch{margin-top:17px}
.welcome h2{margin-top:16px}
.welcome .promise{margin-top:11px}
.start-link{position:absolute;right:140px;top:6px;font-size:20px;line-height:26px;color:var(--link-navy)}

.site-footer{position:absolute;left:0;top:748px;width:1200px;height:212px;
  background:linear-gradient(to bottom,var(--sky-mid),var(--sky-light) 40%,var(--sky-light))}
.footer-frame{position:absolute;left:128px;top:0;width:953px;height:212px;border-left:1px solid var(--rule);border-right:1px solid var(--rule)}
.footer-col{position:absolute;top:0;height:212px}
.col-category{left:0;width:560px;border-right:1px solid var(--rule)}
.col-price{left:560px;width:163px;border-right:1px solid var(--rule)}
.col-search{left:723px;width:229px}
.footer-title{position:absolute;top:2px;font-size:20px;line-height:24px;font-weight:normal;color:var(--white);text-shadow:1px 1px 2px rgba(0,0,0,.6)}
.link-list{position:absolute;top:31px;list-style:none}
.link-list li{font-size:13px;line-height:16px;letter-spacing:.1px}
.link-list a{color:var(--link-navy)}
.search-box{position:absolute;left:17px;top:34px;width:123px;height:18px;border:2px solid #222;border-radius:4px;background:var(--white)}
.search-go{position:absolute;left:143px;top:29px;font-size:20px;line-height:24px;color:var(--link-navy)}
</style>
</head>
<body>
<header class="site-header">
  <div class="brand-name">Insert Logo Here...</div>
  <div class="brand-tagline">Insert Tagline Here....</div>
</header>

<div class="contact-bar">
  <div class="contact-line"><span class="user">Demo User</span> . <span class="phone">(555) 014-2290</span> . <a href="#">info@vexalcart.example</a></div>
</div>

<section class="showcase">
  <div class="product-photo photo-mousepad" role="img" aria-label="Product photo: red gel mouse pad with printed logo"></div>
  <div class="product-photo photo-cooler" role="img" aria-label="Product photo: black and silver cooler bag filled with snacks"></div>
  <div class="product-photo photo-umbrella" role="img" aria-label="Product photo: blue folding umbrella with printed logo"></div>
  <div class="product-photo photo-candy" role="img" aria-label="Product photo: clear gift bag of jelly beans with label"></div>
</section>

<main class="welcome">
  <div class="welcome-inner">
    <h1>Welcome To The Future of Promotional Products!</h1>
    <p class="intro">Gone are the days of searching through dog-eared catalogs or trying to make sense of complicated product websites.</p>
    <p class="pitch">We do the work for you! We've taken only the very best and most current products and placed them in easy-to-use categories designed for your needs. Take a look at our selection - quality products at excellent prices.</p>
    <h2>Enjoy This Amazing New Resource</h2>
    <p class="promise">We know you don't have time to waste; so we've cut to the chase and made it simple! But keep in mind, we do have access to over a mil&shy;lion products - so if you don't see what you're looking for or have a special theme or request, let us know - we'll find it!</p>
  </div>
  <a class="start-link" href="#">Start Shopping</a>
</main>

<footer class="site-footer">
  <div class="footer-frame">
    <div class="footer-col col-category">
      <h3 class="footer-title" style="left:21px">Shop By Category</h3>
      <ul class="link-list" style="left:21px">
        <li><a href="#">Apparel</a></li><li><a href="#">Bags &amp; Totes</a></li><li><a href="#">Caps &amp; Hats</a></li><li><a href="#">Computer</a></li><li><a href="#">Eco Friendly</a></li><li><a href="#">Food, Candy &amp; Drink</a></li><li><a href="#">Golf, Sports &amp; Outdoors</a></li><li><a href="#">Home &amp; Housewares</a></li><li><a href="#">Notebooks &amp; Folios</a></li><li><a href="#">Tools &amp; Hardware</a></li><li><a href="#">Writing Instruments</a></li>
      </ul>
      <ul class="link-list" style="left:199px">
        <li><a href="#">Auto</a></li><li><a href="#">Business Supplies</a></li><li><a href="#">Clocks &amp; Watches</a></li><li><a href="#">Coporate Gifts</a></li><li><a href="#">Electronics</a></li><li><a href="#">Games &amp; Novelties</a></li><li><a href="#">Healthcare &amp; Safety</a></li><li><a href="#">Keychains</a></li><li><a href="#">Pocket &amp; Purse</a></li><li><a href="#">Tradeshows &amp; Events</a></li>
      </ul>
      <ul class="link-list" style="left:358px">
        <li><a href="#">Awards &amp; Recognition</a></li><li><a href="#">Calendars, Books &amp; Cards</a></li><li><a href="#">Company Outings</a></li><li><a href="#">Desktop &amp; Office</a></li><li><a href="#">Executive Gifts</a></li><li><a href="#">Gift Sets</a></li><li><a href="#">Holiday</a></li><li><a href="#">Mugs &amp; Drinkware</a></li><li><a href="#">Stress Balls &amp; Relievers</a></li><li><a href="#">Travel &amp; luggage</a></li>
      </ul>
    </div>
    <div class="footer-col col-price">
      <h3 class="footer-title" style="left:17px">Shop By Price</h3>
      <ul class="link-list" style="left:17px">
        <li><a href="#">Under $5</a></li><li><a href="#">$5 - $10</a></li><li><a href="#">$10 - $20</a></li><li><a href="#">$20 - $50</a></li><li><a href="#">$50 - $100</a></li><li><a href="#">$100 - $200</a></li><li><a href="#">Over $200</a></li>
      </ul>
    </div>
    <div class="footer-col col-search">
      <h3 class="footer-title" style="left:17px">Quick Search</h3>
      <div class="search-box"></div>
      <a class="search-go" href="#">Go</a>
      <h3 class="footer-title" style="left:17px;top:71px">Contact US</h3>
      <ul class="link-list" style="left:17px;top:96px">
        <li><a href="#">info@vexalcart.example</a></li><li><a href="#">www.vexalcart.example</a></li>
      </ul>
    </div>
  </div>
</footer>
</body>
</html>
```